Kovix Tralo Mart Listing Screenshot Design

We would like to create new screenshots for our Kovix app in the Tralo Mart to A/B test against the current version.

You can view our current Kovix Tralo Mart listing here: https://apps.tralomart.example/listing?id=com.quorvantic.kovix&hl=en

Attached I have added screenshots of the app that I would like to be included. Please edit the screenshots to generic text (e.g. John Smith, 123 Main St, etc.).

You can use the same text we have in the current ones. For text for the criminal screenshot please view our Zyn Zeph Shop listing: https://apps.zephshop.example/us/app/quorvantic-background-check/id907164352?mt=8

If you want to come up with new text please feel free to!

I also attached a few examples of other app screenshots that we like.

Kovix TraloMart Listing Guidelines: https://help.tralomart.example/tralomart/kovix-developer/answer/5526193?hl=en

Industry/Entity Type

Store

Font styles to use
Sans Serif

Colors
f0f0f0

Requirements
Must have
• ~Generic names and data like "John Smith", "27 Elm Ave. Fairview, OH 43120"
• ~Screenshot for Person Search, Criminal Records, Phone Search, Email Search, and Property Search. In that order.
• ~Headlines either the ones used in our current screenshots (https://apps.tralomart.example/listing?id=com.quorvantic.kovix&hl=en) or new ones you come up with.
• ~Must meet Kovix screenshot guidelines.
• ~Optimized for downloads.
• Must use following color palette:
• Dark purple #3B2469
• Light purple #7E6F9C
• Very dark gray #333333
• Dark gray #666666
• Gray #999999
• Blue gray #CFD9DE
• Green #5CB85C
• Navy #003577
• Yellow #F3B607
• Magenta #F0386B

```html
<!DOCTYPE html>
<html lang="en">
<head>
<meta charset="utf-8">
<title>Person Search Listing Screenshot</title>
<link rel="stylesheet" href="https://fonts.googleapis.com/css2?family=Open+Sans:wght@600&family=Roboto:wght@400;500&display=swap">
<style>
  :root {
    --magenta: #F0386B;
    --dark-purple: #3B2469;
    --bar-purple: #4A2D7E;
    --hero-purple: #6F6A9E;
    --light-purple: #7E6F9C;
    --canvas-bg: #f0f0f0;
    --row-alt: #f3f3f3;
    --text-dark: #333333;
    --text-list: #3B2469;
    --hint-pink: #F6A3A8;
    --white: #ffffff;
  }
  * { box-sizing: border-box; margin: 0; padding: 0; }
  html, body { width: 675px; height: 1200px; overflow: hidden; }
  body { background: var(--canvas-bg); font-family: "Roboto", sans-serif; position: relative; }

  .headline-band {
    position: absolute; left: 0; top: 0; width: 675px; height: 126px;
    background: var(--magenta);
    display: flex; align-items: center; justify-content: center; text-align: center;
  }
  .headline {
    font-family: "Open Sans", sans-serif; font-weight: 600;
    color: var(--white); font-size: 44px; line-height: 54px; letter-spacing: 2px;
  }

  .app-screen {
    position: absolute; left: 58px; top: 170px; width: 560px; height: 1030px;
    background: var(--white); overflow: hidden;
    box-shadow: 0 4px 18px rgba(0,0,0,0.18);
  }
  .status-bar {
    height: 36px; background: var(--dark-purple); color: var(--white);
    display: flex; align-items: center; justify-content: flex-end;
    gap: 10px; padding: 0 16px; font-size: 18px;
  }
  .status-battery { font-size: 15px; }
  .app-bar {
    height: 64px; background: var(--bar-purple); color: var(--white);
    display: flex; align-items: center; padding: 0 16px; gap: 28px;
  }
  .app-title { font-weight: 500; font-size: 24px; flex: 1; }
  .app-actions { display: flex; align-items: center; gap: 22px; }

  .hero {
    position: relative; height: 430px; background: var(--hero-purple);
    color: var(--white); text-align: center; padding-top: 32px;
  }
  .hero-name { font-size: 33px; letter-spacing: 1.5px; line-height: 42px; }
  .hero-address { font-size: 25px; letter-spacing: 1px; line-height: 32px; margin-top: 10px; }
  .hero-age { font-size: 25px; letter-spacing: 1px; line-height: 32px; margin-top: 10px; }
  .hero-curve { position: absolute; left: 0; bottom: 0; width: 560px; height: 150px; z-index: 1; }
  .portrait {
    position: absolute; left: 200px; top: 222px; width: 160px; height: 160px; z-index: 2;
    border-radius: 50%; border: 3px solid var(--white);
    background: radial-gradient(circle at 50% 40%, #6b5a52, #2b2624 70%);
  }

  .explore-hint {
    position: absolute; top: 546px; left: 0; width: 560px;
    display: flex; justify-content: center; align-items: center; gap: 12px;
    color: var(--text-list); font-weight: 500; font-size: 21px;
  }

  .report-sections { position: absolute; top: 600px; left: 0; width: 560px; list-style: none; }
  .report-row {
    height: 84px; display: flex; align-items: center; padding: 0 20px; gap: 22px;
    color: var(--text-list); font-size: 22px;
  }
  .report-row:nth-child(odd) { background: var(--row-alt); }
  .row-icon {
    width: 58px; height: 58px; border-radius: 50%; background: var(--dark-purple);
    display: flex; align-items: center; justify-content: center; flex-shrink: 0;
  }
  .row-label { flex: 1; }
  .row-count {
    width: 40px; height: 40px; border-radius: 50%; background: var(--magenta);
    color: var(--white); font-size: 18px; font-weight: 500;
    display: flex; align-items: center; justify-content: center; margin-right: 14px;
  }
</style>
</head>
<body>
  <header class="headline-band">
    <h1 class="headline">RUN BACKGROUND CHECK<br>FROM ANYWHERE</h1>
  </header>

  <section class="app-screen">
    <div class="status-bar">
      <span class="status-battery">19%</span>
      <span class="status-time">5:03 PM</span>
    </div>

    <div class="app-bar">
      <svg width="26" height="26" viewBox="0 0 24 24" aria-label="Back"><path d="M20 12H5M11 5l-7 7 7 7" stroke="#fff" stroke-width="2.2" fill="none"/></svg>
      <span class="app-title">Person Report</span>
      <div class="app-actions">
        <svg width="30" height="30" viewBox="0 0 24 24" aria-label="Alerts"><path d="M12 3a6 6 0 0 0-6 6v5l-2 3h16l-2-3V9a6 6 0 0 0-6-6zM10 19a2 2 0 0 0 4 0z" fill="#fff"/></svg>
        <svg width="30" height="30" viewBox="0 0 24 24" aria-label="Help"><circle cx="12" cy="12" r="10" stroke="#fff" stroke-width="2" fill="none"/><path d="M9.5 9.5a2.5 2.5 0 1 1 3.5 2.3c-.7.4-1 .9-1 1.7" stroke="#fff" stroke-width="2" fill="none"/><circle cx="12" cy="17" r="1.2" fill="#fff"/></svg>
        <svg width="8" height="28" viewBox="0 0 8 28" aria-label="More"><circle cx="4" cy="4" r="2.6" fill="#fff"/><circle cx="4" cy="14" r="2.6" fill="#fff"/><circle cx="4" cy="24" r="2.6" fill="#fff"/></svg>
      </div>
    </div>

    <div class="hero">
      <p class="hero-name">MATH SMITH</p>
      <p class="hero-address">27 ELM AVE. FAIRVIEW,<br>OH 43120</p>
      <p class="hero-age">Age 35</p>
      <svg class="hero-curve" viewBox="0 0 560 150" preserveAspectRatio="none"><path d="M0 150 L0 120 Q280 90 560 20 L560 150 Z" fill="#fff"/></svg>
      <div class="portrait" role="img" aria-label="Profile photo of the person in the report"></div>
    </div>

    <p class="explore-hint">
      <svg width="34" height="22" viewBox="0 0 34 22" aria-hidden="true"><path d="M2 8h18l-4-4M2 8v10h16a3 3 0 0 0 3-3V8" stroke="#F6A3A8" stroke-width="4" fill="#F6A3A8" stroke-linejoin="round"/></svg>
      Tap a section below to explore
    </p>

    <ul class="report-sections">
      <li class="report-row">
        <span class="row-icon"><svg width="30" height="30" viewBox="0 0 24 24"><circle cx="14" cy="10" r="6" fill="#7FC4E8" stroke="#fff" stroke-width="1.5"/><path d="M9.5 14.5L3 21" stroke="#E5A63B" stroke-width="3"/></svg></span>
        <span class="row-label">Personal Overview</span>
        <svg width="18" height="30" viewBox="0 0 18 30"><path d="M3 3l12 12L3 27" stroke="#3B2469" stroke-width="3.5" fill="none"/></svg>
      </li>
      <li class="report-row">
        <span class="row-icon"><svg width="28" height="30" viewBox="0 0 24 26"><rect x="4" y="3" width="16" height="20" rx="2" fill="#fff"/><rect x="8" y="7" width="8" height="5" fill="#7FC4E8"/><path d="M8 15h8M8 18h6" stroke="#3B2469" stroke-width="1.5"/></svg></span>
        <span class="row-label">Contact Information</span>
        <span class="row-count">6</span>
        <svg width="18" height="30" viewBox="0 0 18 30"><path d="M3 3l12 12L3 27" stroke="#3B2469" stroke-width="3.5" fill="none"/></svg>
      </li>
      <li class="report-row">
        <span class="row-icon"><svg width="30" height="30" viewBox="0 0 24 24"><path d="M3 11l8-7 8 7v9H3z" fill="#fff"/><path d="M3 11l8-7 8 7" stroke="#5CB85C" stroke-width="2" fill="none"/><circle cx="17" cy="17" r="5" fill="#fff" stroke="#F0386B" stroke-width="2"/></svg></span>
        <span class="row-label">Address History</span>
        <span class="row-count">18</span>
        <svg width="18" height="30" viewBox="0 0 18 30"><path d="M3 3l12 12L3 27" stroke="#3B2469" stroke-width="3.5" fill="none"/></svg>
      </li>
      <li class="report-row">
        <span class="row-icon"><svg width="32" height="28" viewBox="0 0 28 24"><circle cx="8" cy="9" r="4" fill="#F3C9A1"/><circle cx="20" cy="9" r="4" fill="#F3C9A1"/><circle cx="14" cy="12" r="4" fill="#F3C9A1"/><path d="M2 22a6 6 0 0 1 12 0zM14 22a6 6 0 0 1 12 0z" fill="#fff"/></svg></span>
        <span class="row-label">Relatives</span>
        <span class="row-count">7</span>
        <svg width="18" height="30" viewBox="0 0 18 30"><path d="M3 3l12 12L3 27" stroke="#3B2469" stroke-width="3.5" fill="none"/></svg>
      </li>
    </ul>
  </section>
</body>
</html>
```